Business card design needed

Hello, I Need a business card for a company that specialises in providing contract management services for civil construction projects - roads, bridges etc.
I do have a logo that i produced for PLOVER Civilworks however it probably needs a little work, the circles dont have defined edges, i was thinking the colours should reflect the dry interior of Australia progressing out to the colours of the ocean as you move towards the East.... that was my thinking anyway!
Target Market(s)
Professional people generally 30+ yrs old who need professional services to deliver contracts in a high risk environment
Industry/Entity Type
Construction
Contact Information for Business Card
PLOVER Civilworks
Darren Holbeck - Director and Principal Engineer
Registered Professional Engineer of Queensland
Phone 0438 615 272
Email darren@plovercivilworks.com.au
ABN 83 214 570 618
Logo Text
PLOVER Civilworks
Logo styles of interest
Pictorial/Combination Logo
Wordmark Logo
Lettermark Logo
Look and feel

```html
<!DOCTYPE html>
<html lang="en">
<head>
<meta charset="utf-8">
<title>PLOVER Civilworks – Business Card</title>
<link rel="stylesheet" href="https://fonts.googleapis.com/css2?family=Roboto:wght@300;400;500;700&display=swap">
<style>
  :root {
    --backdrop: #e4e5e7;
    --card: #ffffff;
    --navy: #0b4a86;
    --olive: #8f9a5c;
    --ink: #1f1f1f;
    --muted: #4a4a4a;
    --rule: #6a7fa6;
    --band-1: #d8d9db;
    --band-2: #e1e2e3;
    --band-3: #e9eaea;
    --band-4: #f1f1f1;
  }
  * { margin: 0; padding: 0; box-sizing: border-box; }
  html, body {
    width: 1200px; height: 883px; overflow: hidden;
    background: var(--backdrop);
    font-family: "Roboto", Arial, sans-serif;
  }
  .card {
    position: absolute; left: 75px; top: 148px;
    width: 1050px; height: 587px;
    background: var(--card);
    overflow: hidden;
  }
  .bands { position: absolute; left: 0; top: 0; }
  .brand {
    position: absolute; right: 144px; top: 48px;
    text-align: right; color: var(--navy); font-weight: 500;
    line-height: 0.95;
  }
  .brand-main { display: block; font-size: 104px; letter-spacing: 2px; }
  .brand-sub { display: block; font-size: 66px; margin-top: 6px; }
  .marker {
    position: absolute; left: 60px; top: 380px;
    width: 20px; height: 57px; background: var(--olive);
  }
  .person { position: absolute; left: 92px; top: 379px; }
  .person-name { font-size: 25px; font-weight: 700; color: var(--ink); line-height: 34px; }
  .person-role { font-size: 25px; font-weight: 300; color: var(--ink); line-height: 34px; }
  .contact { position: absolute; left: 552px; top: 375px; }
  .contact-line { font-size: 27px; font-weight: 300; color: var(--ink); line-height: 36px; white-space: nowrap; }
  .contact-line.email { font-size: 25px; }
  .contact-key { font-weight: 700; color: var(--navy); margin-right: 8px; }
  .abn { font-size: 18px; font-weight: 400; color: var(--muted); margin-top: 4px; margin-left: 2px; }
  .registration {
    position: absolute; left: 140px; top: 512px;
    width: 751px; height: 45px;
    border-top: 1.5px solid var(--rule);
    border-bottom: 1.5px solid var(--rule);
    display: flex; align-items: center; justify-content: center;
    font-size: 22px; font-weight: 300; color: var(--muted);
    letter-spacing: 0.6px;
  }
</style>
</head>
<body>
  <main class="card">
    <svg class="bands" width="470" height="292" viewBox="0 0 470 292" aria-hidden="true">
      <rect x="0" y="0" width="66" height="292" fill="var(--band-1)"/>
      <rect x="88" y="0" width="96" height="292" fill="var(--band-2)"/>
      <rect x="212" y="0" width="96" height="292" fill="var(--band-3)"/>
      <rect x="336" y="0" width="96" height="292" fill="var(--band-4)"/>
    </svg>

    <div class="brand">
      <span class="brand-main">PLOVER</span>
      <span class="brand-sub">Civilworks</span>
    </div>

    <span class="marker"></span>
    <div class="person">
      <p class="person-name">Darren Holbeck</p>
      <p class="person-role">Director &amp; Principal Engineer</p>
    </div>

    <div class="contact">
      <p class="contact-line"><span class="contact-key">P</span>0438 615 272</p>
      <p class="contact-line email"><span class="contact-key">E</span>darren@plovercivilworks.com.au</p>
      <p class="abn">ABN 83 214 570 618</p>
    </div>

    <p class="registration">REGISTERED PROFESSIONAL ENGINEER OF QUEENSLAND</p>
  </main>
</body>
</html>
```